Business Card Design

We recently had a new logo designed by Pixel Harbor. Now we want to create new business cards and letterhead that compliment our new logo.

We are audiologists in private practice specializing in hearing evaluations and fitting hearing aids. We want a clean and professional card.

We need business cards for each audiologist. The names and titles are:
Marnie Ostrova, AuD
Audiologist

Jen Tarbel, AuD
Audiologist

Corvina Plesk, AuD
Audiologist

We also need a business card with no provider. Just a generic one.

Finally, we need an appointment card. This is what the front desk uses to give to the patient with their next appointment date and time.

Target Market(s)

Our clients tend to be highly educated. They are older so the cards should be clean and easy to read. No squirrely font please.

Industry/Entity Type

Business

Contact Information for Business Card

20731 8th Ave NE, suite 417
Seattle, WA 98177
206-592-8074

Requirements
Must have
• Clean
Easy to read
Professional
Modern but approachable / warm
Should not have
• Other pictures besides the logo

```html
<!DOCTYPE html>
<html lang="en">
<head>
<meta charset="utf-8">
<title>Lakecrest Hearing Services – Business Card</title>
<link href="https://fonts.googleapis.com/css2?family=Barlow:wght@400;500&display=swap" rel="stylesheet">
<style>
  :root {
    --page-bg: #eeefee;
    --navy: #11426a;
    --teal: #35ac98;
    --card-white: #ffffff;
    --ink: #2b2d30;
    --ink-soft: #4a4c50;
    --on-teal: #e9f6f3;
  }
  * { margin: 0; padding: 0; box-sizing: border-box; }
  html, body {
    width: 1200px; height: 900px; overflow: hidden;
    background: var(--page-bg);
    font-family: "Barlow", Arial, sans-serif;
  }
  .canvas { position: relative; width: 1200px; height: 900px; }

  .card {
    position: absolute; left: 300px; width: 600px; height: 343px;
    background: var(--card-white);
    box-shadow: 3px 4px 6px rgba(0,0,0,0.28);
  }
  .card--front { top: 80px; }
  .card--back { top: 476px; }

  .band { position: absolute; left: 0; width: 100%; height: 75px; }
  .band--navy { top: 0; background: var(--navy); }
  .band--teal { bottom: 0; background: var(--teal); }

  .brand {
    position: absolute; display: flex; align-items: center; gap: 12px;
  }
  .brand__dot {
    width: 40px; height: 40px; border-radius: 50%;
    background: var(--teal); flex: none;
  }
  .brand__name {
    font-weight: 500; font-size: 19px; line-height: 1.15;
    color: var(--ink); letter-spacing: 0.5px; text-transform: uppercase;
  }
  .card--front .brand { left: 200px; top: 152px; }
  .card--back .brand { left: 26px; top: 152px; }

  .website {
    position: absolute; left: 0; right: 0; bottom: 30px;
    text-align: center; color: var(--on-teal);
    font-size: 14px; letter-spacing: 3.2px;
  }

  .provider {
    position: absolute; right: 31px; top: 152px; text-align: right;
  }
  .provider__name {
    font-size: 25px; font-weight: 400; color: var(--ink);
    letter-spacing: 0.6px; line-height: 1;
  }
  .provider__title {
    font-size: 12px; color: var(--ink-soft); margin-top: 4px; letter-spacing: 0.3px;
  }

  .contact {
    position: absolute; right: 31px; bottom: 11px; text-align: right;
    list-style: none; color: var(--on-teal); font-size: 12px;
    line-height: 20px; letter-spacing: 0.3px;
  }
</style>
</head>
<body>
<main class="canvas">
  <section class="card card--front" aria-label="Business card front">
    <div class="band band--navy"></div>
    <div class="brand">
      <span class="brand__dot"></span>
      <span class="brand__name">Lakecrest<br>Hearing Services</span>
    </div>
    <div class="band band--teal">
      <p class="website">www.lakecresthearing.com</p>
    </div>
  </section>

  <section class="card card--back" aria-label="Business card back">
    <div class="band band--navy"></div>
    <div class="brand">
      <span class="brand__dot"></span>
      <span class="brand__name">Lakecrest<br>Hearing Services</span>
    </div>
    <div class="provider">
      <p class="provider__name">MARNIE OSTROVA, AuD</p>
      <p class="provider__title">Audiologist</p>
    </div>
    <div class="band band--teal">
      <ul class="contact">
        <li>206-592-8074</li>
        <li>20731 8th Avenue NE,suite 417</li>
        <li>Seattle. WA 98177</li>
      </ul>
    </div>
  </section>
</main>
</body>
</html>
```